Income Tax and Accounting Brochure

I need a brochure using my new logo (file attached). I do tax work and accounting work. I am an EA (QDX Enrolled Agent - logo attached) and would like this incorporated into the brochure. I also have a MSA in Accounting. Please incorporate the text that I have provided in the brochure.

Target Market(s)

Tax Clients - both business and individuals

Industry/Entity Type

Accounting

Colors
0054AA
0677BA
7BADD7
CADEEF
E8F1F8

Requirements
Must have
• Use my logo and the QDX EA file in the brochure
Nice to have
• I would like to see a brochure that I can customize with my own text if possible.

```html
<!DOCTYPE html>
<html lang="en">
<head>
<meta charset="utf-8">
<title>Halvern Accounting &amp; Consulting – Tax Flyer</title>
<link rel="stylesheet" href="https://fonts.googleapis.com/css2?family=Roboto:ital,wght@0,400;0,500;0,700;1,400&family=Montserrat:wght@500&display=swap">
<style>
:root{
  --backdrop:#a5a7ac;
  --paper:#ffffff;
  --brand-blue:#0054aa;
  --brand-mid:#0677ba;
  --brand-light:#7badd7;
  --brand-red:#c8102e;
  --bar-dark:#1d2230;
  --ink:#2b2b2b;
}
*{box-sizing:border-box;margin:0;padding:0}
html,body{width:1200px;height:851px;overflow:hidden}
body{background:var(--backdrop);font-family:'Roboto',sans-serif;color:var(--ink);position:relative}
.page{position:absolute;top:108px;width:453px;height:640px;background:var(--paper);overflow:hidden;box-shadow:0 6px 14px rgba(0,0,0,.25)}
.page--front{left:129px}
.page--back{left:637px}

.wordmark{font-family:'Montserrat',sans-serif;font-weight:500;color:var(--brand-blue);display:flex;align-items:center;gap:8px}
.wordmark__dot{width:44px;height:44px;border-radius:50%;background:var(--brand-blue);flex:none}
.wordmark__text{line-height:1.25;letter-spacing:.8px}
.wordmark__text span{display:block}
.wordmark__line1{font-size:13px}
.wordmark__line2{font-size:10px;letter-spacing:2.6px}

/* front */
.hero{position:absolute;left:0;top:0;width:453px;height:351px;background:linear-gradient(135deg,#8a8580 0%,#b9b3ad 35%,#d9d6d2 60%,#c7c4c1 100%)}
.hero__logo-panel{position:absolute;right:0;top:0;width:256px;height:75px;background:rgba(255,255,255,.94);clip-path:polygon(10% 0,100% 0,100% 100%,0 100%);display:flex;align-items:center;justify-content:flex-end;padding-right:20px}
.hero__rule{position:absolute;left:0;top:351px;width:453px;height:5px;background:var(--brand-blue);border-top:1px solid var(--brand-light)}

.section-bar{position:absolute;left:41px;width:370px;height:21px;background:var(--bar-dark);color:#fff;font-weight:700;font-size:12.5px;display:flex;align-items:center;padding-left:27px}
.section-bar::before{content:"";position:absolute;left:-2px;top:-1px;width:23px;height:23px;border-radius:50%;background:var(--brand-blue);border:2px solid #fff;box-shadow:0 0 0 1px var(--brand-light)}

.about__portrait{position:absolute;left:41px;top:422px;width:95px;height:138px;background:linear-gradient(180deg,#1c1c1c 0%,#4a3a30 45%,#6d6a6c 100%)}
.about__copy{position:absolute;left:147px;top:421px;width:265px;font-size:8.6px;line-height:11.4px;text-align:justify}
.about__name{font-size:12px;font-weight:700;color:var(--brand-blue);margin-bottom:3px;text-align:left}
.about__role{font-weight:400;font-style:italic;color:var(--brand-red)}
.about__copy p+p{margin-top:11px}

.front-footer{position:absolute;left:0;bottom:0;width:453px;height:43px;background:var(--brand-blue);border-top:4px solid var(--brand-red);box-shadow:0 -2px 0 #fff inset;display:flex;align-items:center;justify-content:center;gap:8px;color:#fff;font-weight:500;font-size:15.5px;letter-spacing:.2px}
.front-footer svg{width:15px;height:15px;flex:none}

/* back */
.back-logo{position:absolute;left:0;right:0;top:32px;display:flex;justify-content:center}
.back-logo .wordmark__dot{width:52px;height:52px}
.back-logo .wordmark__line1{font-size:15px}
.back-logo .wordmark__line2{font-size:11.5px;letter-spacing:3px}

.body-copy{position:absolute;left:41px;width:370px;font-size:8.6px;line-height:11.4px;text-align:justify}
.body-copy p+p{margin-top:11px}
.body-copy h3{font-size:8.6px;font-weight:500;margin-bottom:2px}

.benefits{position:absolute;left:41px;top:410px;width:370px;list-style:none}
.benefits{top:409px}
.benefit-list{position:absolute;left:41px;top:410px;width:370px;list-style:none}
.benefit-list::before{content:"";position:absolute;left:4px;top:8px;bottom:8px;width:1px;background:var(--brand-light)}
.benefit{position:relative;padding-left:14px;font-size:8.6px;line-height:11.4px;text-align:justify}
.benefit+.benefit{margin-top:11px}
.benefit svg{position:absolute;left:0;top:1px;width:9px;height:9px}

.back-footer{position:absolute;left:0;bottom:0;width:453px;height:86px;background:linear-gradient(90deg,var(--brand-blue),var(--brand-mid));border-top:4px solid var(--brand-red);box-shadow:0 2px 0 #fff inset;color:#fff}
.back-footer__address{position:absolute;left:36px;top:26px;font-size:9.6px;line-height:11.5px}
.back-footer__address strong{font-weight:500}
.back-footer__contact{position:absolute;right:42px;top:22px;text-align:right;font-weight:700}
.back-footer__phone{font-size:21px;line-height:22px;display:flex;align-items:center;gap:6px;justify-content:flex-end}
.back-footer__web{font-size:14px;display:flex;align-items:center;gap:8px;justify-content:flex-end;margin-top:1px}
.back-footer svg{width:14px;height:14px}
</style>
</head>
<body>

<section class="page page--front">
  <div class="hero" role="img" aria-label="Photo of a woman in a grey blazer using a calculator over invoices at an office desk">
    <div class="hero__logo-panel">
      <div class="wordmark">
        <span class="wordmark__dot"></span>
        <div class="wordmark__text"><span class="wordmark__line1">HALVERN ACCOUNTING</span><span class="wordmark__line2">&amp; CONSULTING, LLC</span></div>
      </div>
    </div>
  </div>
  <div class="hero__rule"></div>

  <div class="section-bar" style="top:390px">About</div>
  <div class="about__portrait" role="img" aria-label="Portrait of the principal"></div>
  <div class="about__copy">
    <div class="about__name">Marian T Colbeck, MSA EA <span class="about__role">(Principal)</span></div>
    <p>I have a Masters' Degree in accounting and am an QDX Enrolled Agent. I am also a LedgerBooks Advanced Certified Consultant in both the online and desktop products including Enterprise and Point of Sale. I provide individual and small business tax services, Accounting, bookkeeping, QDX representation, insurance audit representation, business license assistance and more.</p>
    <p>I have experience working with a wide variety of clients from the point where they first decide they want to start a business. They are often unsure about what to do first- I have a lot of experience to offer you.</p>
  </div>

  <footer class="front-footer">
    <svg viewBox="0 0 24 24" fill="#fff"><path d="M6.6 10.8a15 15 0 0 0 6.6 6.6l2.2-2.2c.3-.3.7-.4 1-.2 1.1.4 2.3.6 3.6.6.6 0 1 .4 1 1V20c0 .6-.4 1-1 1A17 17 0 0 1 3 4c0-.6.4-1 1-1h3.5c.6 0 1 .4 1 1 0 1.3.2 2.5.6 3.6.1.3 0 .7-.2 1z"/></svg>
    <span>(555)014-7720</span>
    <svg viewBox="0 0 24 24" fill="none" stroke="#fff" stroke-width="1.6"><circle cx="12" cy="12" r="9.5"/><ellipse cx="12" cy="12" rx="4" ry="9.5"/><path d="M2.5 12h19M4 7h16M4 17h16"/></svg>
    <span>WWW.HALVERNACCOUNTING.COM</span>
  </footer>
</section>

<section class="page page--back">
  <div class="back-logo">
    <div class="wordmark">
      <span class="wordmark__dot"></span>
      <div class="wordmark__text"><span class="wordmark__line1">HALVERN ACCOUNTING</span><span class="wordmark__line2">&amp; CONSULTING, LLC</span></div>
    </div>
  </div>

  <div class="section-bar" style="top:113px">What a joy it is to watch success in action!</div>
  <div class="body-copy" style="top:148px">
    <h3>Tax Preparation – why hire us?</h3>
    <p>Preparing your own income tax return can be a task that leaves you with more questions than answers. According to a study released by the US Government's Federal Audit Review Office last year, most taxpayers (77% of 71 million taxpayers) believe they benefited from using a professional tax preparer.</p>
    <p>Whether we like it or not, today's tax laws are so complicated that filing a relatively simple return can be confusing. It is just too easy to overlook deductions and credits to which you are entitled. Even if you use a computer software program there's no substitute for the assistance of an experienced tax professional.</p>
  </div>

  <div class="section-bar" style="top:269px">Here's what your get...</div>
  <ul class="benefit-list" style="top:307px">
    <li class="benefit"><svg viewBox="0 0 10 10"><circle cx="5" cy="5" r="5" fill="#c8102e"/><path d="M2.6 5.1 4.3 6.7 7.4 3.4" stroke="#fff" stroke-width="1.3" fill="none"/></svg>Your tax return will be checked and rechecked by our computer software identifying potential problems the QDX may look at more closely and reviewing the math to limit QDX contacts.</li>
    <li class="benefit"><svg viewBox="0 0 10 10"><circle cx="5" cy="5" r="5" fill="#c8102e"/><path d="M2.6 5.1 4.3 6.7 7.4 3.4" stroke="#fff" stroke-width="1.3" fill="none"/></svg>Your tax return can be filed electronically so you will get a refund back quicker.</li>
    <li class="benefit"><svg viewBox="0 0 10 10"><circle cx="5" cy="5" r="5" fill="#c8102e"/><path d="M2.6 5.1 4.3 6.7 7.4 3.4" stroke="#fff" stroke-width="1.3" fill="none"/></svg>Our staff will show you how to adjust your payroll withholding to get more money back each week. Why give the QDX an interest free loan for up to 16 months.</li>
    <li class="benefit"><svg viewBox="0 0 10 10"><circle cx="5" cy="5" r="5" fill="#c8102e"/><path d="M2.6 5.1 4.3 6.7 7.4 3.4" stroke="#fff" stroke-width="1.3" fill="none"/></svg>We will show you potential deductions to limit your tax liability for next year. In addition, we will give you a sheet of commonly overlooked deductions to limit the following year's tax liability.</li>
  </ul>

  <div class="section-bar" style="top:451px">Books a Mess: No Problem!</div>
  <div class="body-copy" style="top:489px">
    <p>If you own a small business and haven't kept up your bookkeeping, don't worry. We can help you. We'll prepare your bookkeeping for the year, prepare a full Schedule C, as well as your personal income tax return. Then we'll help you set up an easy system that allows you to keep your books in tip-top shape next year.</p>
  </div>

  <footer class="back-footer">
    <div class="back-footer__address">
      <strong>Halvern Accounting &amp; Consulting, LLC</strong><br>
      2280 Fenwick Hollow Rd, PO Box 41<br>
      Ashbury, VA 20000
    </div>
    <div class="back-footer__contact">
      <div class="back-footer__phone"><svg viewBox="0 0 24 24" fill="#fff"><path d="M6.6 10.8a15 15 0 0 0 6.6 6.6l2.2-2.2c.3-.3.7-.4 1-.2 1.1.4 2.3.6 3.6.6.6 0 1 .4 1 1V20c0 .6-.4 1-1 1A17 17 0 0 1 3 4c0-.6.4-1 1-1h3.5c.6 0 1 .4 1 1 0 1.3.2 2.5.6 3.6.1.3 0 .7-.2 1z"/></svg>(555)014-7720</div>
      <div class="back-footer__web"><svg viewBox="0 0 24 24" fill="none" stroke="#fff" stroke-width="1.6"><circle cx="12" cy="12" r="9.5"/><ellipse cx="12" cy="12" rx="4" ry="9.5"/><path d="M2.5 12h19M4 7h16M4 17h16"/></svg>HALVERNACCOUNTING.COM</div>
    </div>
  </footer>
</section>

</body>
</html>
```